Homepage Redesign for Healthcare Tech Company

This is for a redesign of our current homepage. We have specific notes and a Mockup and we need a great designer to bring it to life and make it look sophisticated and professional. Please see the Current Page (attached and online) as well as the Notes doc and Mockup PPT, both attached, for what we need.

Overall, look at the current page as a sketch of what it could be. We would like a design that really nails the structure of both the overall page and the pipeline (that runs through Sections 1-4), so that it looks like one, clean, custom design (not pieced together). It’s important that the basic structure of the pipeline, especially the transition from icons to screenshots (starting in section 2, and mostly in section 3) all flow together well and look like a deliberate, well thought-out design. Please include that, and at least the headlines for each section, in any initial submissions.

We will be building out of website beyond just this page, and would be great to work with a designer we can continue working with on the website, the graphical screenshots and some infographics. Not a must but definitely an option if you would like. We didn’t include all pages in this project, because we would like the designer to focus all energy on creating a well thought-out homepage design with the wow factor, and we can build it out together from there. For now, we would like just 2 additional general theme pages (one smaller page for a couple paragraphs of text only and one with a few uniform sections, with room for text and small graphic-see notes).

Our customers are healthcare companies – both Doctors and IT professionals of medium to large healthcare organizations who support doctors. We are experts in healthcare interoperability technology and the page should reflect that. Medical Record documentation is an expensive time-consuming massive headache for our customer base. What we are offering is a truly groundbreaking solution that leverages the best technology available to bring them something that wasn’t possible before – ALL of their patient data in one enriched and linked document, delivered to their current workflow. It's an expensive solution but very impactful in terms of better patient care and dramatically streamlined workflow - the homepage needs to reflect that. Please take the time to understand the solution we offer and just let me know if you need clarification – I’m happy to answer any questions.

Thanks!

SEE ATTACHMENTS, and also this more detailed breakdown of the sections: https://qv.fx/Tr4mPz

Target Market(s)

Doctors, IT Professionals in the Healthcare field, Medical Coders..but focus should be on Doctors

Number of Pages Required

1 page

Colors
0355a3
3276b5
0293ce
6b449b
886aae
b7a5cd
00a990
33b8a4
86cfc6

Requirements
Must have
• - Sophisticated, professional, masterful layout
- Must refer to the attached DESIGN NOTES.doc (about 2 pages) and MOCKUP.PPT but bring the idea to life in an innovative way. In general, we collect all medical records, summarize and unify into 1 document that we send straight into each patient file, but referring to the actual notes to truly get what we do and what we need it is a must.
- Framing/background emphasis for provided screenshots (even if these screenshots don't fit exactly, we will make them fit after)
- Emphasis on the fact that clicking the View Source buttons in the Lumora (what we call our product) opens the actual source documents (underlying medical record) - this is a big deal for doctors and medical coders.
- Final design should be in editable PSD file
Nice to have
• Animation. We are asking for design only because we want the best design possible but we would definitely choose a great animated design (assuming that means you'd need to code it too - let me know) and ensure that you are paid the extra for coding if you need to code it yourself.
Should not have
• template feel - should look custom
cheesy photos of models dressed as doctors

```html
<!DOCTYPE html>
<html lang="en">
<head>
<meta charset="utf-8">
<title>Corvanta — Unified Patient Intelligence</title>
<link href="https://fonts.googleapis.com/css2?family=Montserrat:wght@400;500;600;700;800&display=swap" rel="stylesheet">
<style>
:root{
  --navy-900:#0a1727;
  --navy-800:#0c1d31;
  --navy-700:#0b2744;
  --navy-600:#0d2f52;
  --navy-500:#123a63;
  --teal:#22d1b4;
  --teal-soft:#33b8a4;
  --teal-pale:#86cfc6;
  --blue:#0293ce;
  --blue-mid:#3276b5;
  --purple:#6b449b;
  --purple-mid:#886aae;
  --purple-card:#8b70cf;
  --purple-pale:#b7a5cd;
  --white:#ffffff;
  --text:#d9e4ef;
  --muted:#aebfd0;
  --bar:#1fc7b2;
}
*{box-sizing:border-box;margin:0;padding:0}
html,body{width:1200px;height:4758px;overflow:hidden;background:var(--navy-900)}
body{font-family:"Montserrat",sans-serif;color:var(--text)}
.page{position:relative;width:1200px;height:4758px;overflow:hidden}
section,footer,header{position:relative;width:1200px}
.abs{position:absolute}
.center{left:0;width:1200px;text-align:center}
.edge{position:absolute;left:0;top:0;width:1200px;height:70px}

.btn{display:inline-block;background:var(--purple-mid);color:var(--white);font-size:12px;font-weight:500;padding:8px 16px;border-radius:3px;border:1px solid var(--purple-pale)}
.section-title{font-size:28px;font-weight:700;letter-spacing:1px;color:var(--white);text-transform:uppercase;line-height:1.22}
.section-lead{font-size:11.5px;line-height:1.85;color:var(--text)}

/* hero */
.hero{height:610px;background:radial-gradient(ellipse at 50% 30%,#12304d 0%,var(--navy-800) 60%,var(--navy-900) 100%)}
.nav a{position:absolute;top:19px;font-size:11.5px;color:var(--text);text-decoration:none}
.brand{position:absolute;top:12px;left:0;width:1200px;text-align:center;font-size:24px;font-weight:500;letter-spacing:1px;color:var(--white)}
.brand .mark{display:inline-block;width:22px;height:22px;background:var(--purple-mid);vertical-align:-3px;margin-right:9px}
.nav .outline{left:951px;top:12px;border:1px solid var(--white);padding:6px 10px;font-size:11px}
.hero-title{top:166px;font-size:41px;font-weight:800;letter-spacing:1.5px;color:var(--teal)}
.hero-sub{top:222px;font-size:16px;font-weight:600;color:var(--white);line-height:1.3}
.hero-copy{top:306px;font-size:12px;line-height:1.75;color:var(--text)}
.hero-btn{top:406px}
.scroll-pill{left:590px;top:546px;width:20px;height:36px;border-radius:10px;background:var(--teal)}

/* sources */
.sources{height:922px;background:linear-gradient(180deg,var(--navy-600),var(--navy-700))}
.source{position:absolute;width:250px;font-size:11px;line-height:1.85;color:var(--text)}
.source h3{font-size:17px;font-weight:500;color:var(--teal);margin-bottom:6px;letter-spacing:.3px}
.source.left{text-align:right;left:138px}
.source.right{text-align:left;left:812px}
.icon{position:absolute}

/* transform */
.transform{height:608px;background:radial-gradient(ellipse at 50% 60%,#0f2c4c 0%,var(--navy-800) 75%)}
.logo-ring{left:554px;top:1901px}
.ccda-frame{left:408px;top:453px;width:384px;height:180px;border:2px solid var(--teal-soft);padding:10px;background:rgba(16,60,100,.35)}
.ccda-panel{width:100%;height:100%;background:linear-gradient(180deg,#2e6fb0 0%,#1a4f8c 100%);position:relative;text-align:center;color:var(--white)}
.ccda-head{height:20px;background:#e8eef5}
.ccda-panel h4{font-size:15px;font-weight:700;margin-top:24px}
.ccda-panel p{font-size:11.5px;line-height:1.7;margin-top:6px;padding:0 10px}

/* insights */
.insights{height:740px;background:linear-gradient(180deg,var(--navy-700),var(--navy-600))}
.feature-ring{position:absolute;width:80px;height:80px;border-radius:50%;border:2px solid var(--teal);display:flex;align-items:center;justify-content:center}
.insight{position:absolute;left:140px;width:250px;font-size:11.5px;line-height:1.8}
.insight h3{font-size:14px;font-weight:700;color:var(--teal);margin-bottom:6px}
.shot{position:absolute;background:linear-gradient(180deg,#f6f8fb,#dfe6ee);box-shadow:0 4px 18px rgba(0,0,0,.45)}
.shot.framed{border:2px solid var(--teal-soft)}

/* ehr */
.ehr{height:535px;background:linear-gradient(180deg,var(--navy-600) 0%,var(--navy-800) 100%)}
.vendor-grid{position:absolute;left:140px;top:162px;display:grid;grid-template-columns:repeat(3,123px);gap:10px 10px}
.vendor{height:65px;background:var(--white);display:flex;align-items:center;justify-content:center;font-size:14px;font-weight:600;color:#2b4a6b;gap:6px}
.vendor .dot{width:10px;height:10px;border-radius:50%;background:#2b4a6b}
.ehr-title{left:600px;top:190px;width:440px;font-size:26px;font-weight:700;letter-spacing:1px;color:var(--white);line-height:1.22}
.ehr-copy{left:600px;top:300px;width:380px;font-size:11.5px;line-height:1.8}

/* features */
.features{height:480px;background:var(--navy-800)}
.card{position:absolute;top:76px;width:209px;border:1.5px solid #2a7f93;border-radius:4px;background:#0c2038;text-align:center;padding:36px 14px 20px}
.card.active{background:var(--purple-card);border-color:var(--purple-pale)}
.card h3{font-size:13px;font-weight:600;color:var(--teal);letter-spacing:.6px;margin:26px 0 8px;line-height:1.35}
.card.active h3{color:var(--white)}
.card p{font-size:11px;line-height:1.85;color:var(--text)}
.card svg{display:block;margin:0 auto}

/* blog */
.blog{height:628px;background:linear-gradient(180deg,var(--navy-700),var(--navy-600))}
.post{position:absolute;top:105px;width:283px;height:325px;border:1.5px solid #2a7f93;border-radius:3px;background:#0c2540;overflow:hidden}
.post .photo{height:172px}
.post .date{position:absolute;left:16px;top:4px;width:30px;background:var(--blue-mid);color:var(--white);text-align:center;font-weight:700;font-size:17px;line-height:1;padding:3px 0}
.post .date small{display:block;font-size:8px;font-weight:600}
.post h4{font-size:13px;font-weight:700;color:var(--white);line-height:1.45;margin:30px 18px 6px}
.post p{font-size:10.5px;line-height:1.6;margin:0 18px}
.post .more{display:block;margin:18px 18px 0;font-size:11px;font-weight:700;color:var(--teal);letter-spacing:.6px}
.arrow{position:absolute;top:4140px;width:36px;height:36px;border-radius:50%;border:2px solid var(--teal);display:flex;align-items:center;justify-content:center}

/* about & bar */
.about{height:193px;background:var(--navy-900)}
.about p{font-size:11px;line-height:1.95;color:var(--text)}
.legal{height:42px;background:var(--bar);text-align:center;font-size:11px;line-height:42px;color:var(--navy-800);font-weight:500}

.pipeline{position:absolute;left:0;top:0;width:1200px;height:4758px;z-index:1;pointer-events:none}
.front{z-index:2}
</style>
</head>
<body>
<div class="page">

<svg class="pipeline" viewBox="0 0 1200 4758" aria-hidden="true">
  <defs>
    <filter id="glow" x="-50%" y="-50%" width="200%" height="200%"><feGaussianBlur stdDeviation="2.5" result="b"/><feMerge><feMergeNode in="b"/><feMergeNode in="SourceGraphic"/></feMerge></filter>
  </defs>
  <g stroke="#22d1b4" stroke-width="2" fill="none" filter="url(#glow)">
    <line x1="594" y1="905" x2="594" y2="1855"/>
    <line x1="606" y1="905" x2="606" y2="1855"/>
    <polyline points="402,845 594,905"/>
    <polyline points="797,845 606,905"/>
    <polyline points="402,1274 594,1357"/>
    <polyline points="797,1274 606,1357"/>
    <line x1="600" y1="1946" x2="600" y2="1985"/>
    <line x1="220" y1="2410" x2="452" y2="2410"/>
    <line x1="220" y1="2630" x2="452" y2="2630"/>
    <polyline points="845,2345 798,2345 798,2790 845,2790"/>
    <line x1="748" y1="2560" x2="845" y2="2560"/>
  </g>
  <g stroke="#3a64b8" stroke-width="1.6" fill="none">
    <polyline points="402,1071 594,1130"/>
    <polyline points="797,1071 606,1130"/>
  </g>
  <g fill="#22d1b4">
    <circle cx="402" cy="845" r="4"/><circle cx="797" cy="845" r="4"/>
    <circle cx="402" cy="1274" r="4"/><circle cx="797" cy="1274" r="4"/>
  </g>
  <g fill="#5b7fd0"><circle cx="402" cy="1071" r="3.5"/><circle cx="797" cy="1071" r="3.5"/></g>
</svg>

<!-- HERO -->
<header class="hero">
  <nav class="nav">
    <a href="#" style="left:143px">About</a>
    <a href="#" style="left:224px">Features</a>
    <a href="#" style="left:317px">Process</a>
    <div class="brand"><span class="mark"></span>CORVANTA</div>
    <a href="#" style="left:792px">Team</a>
    <a href="#" style="left:867px">Clients</a>
    <a href="#" class="outline">Request Access</a>
  </nav>
  <h1 class="abs center hero-title">UNIFIED PATIENT INTELLIGENCE</h1>
  <p class="abs center hero-sub">Each patients’ full medical history, summary and analysis in one<br>comprehensive health record</p>
  <p class="abs center hero-copy">Corvanta collects patients’ records from all sources of external clinical data, synthesizes the captured data into one<br>composite health record, abstracts all HCC, MIPS and HEDIS opportunities, and delivers them directly into your EHR,<br>all in a matter of hours.</p>
  <div class="abs center hero-btn"><a class="btn">Request Access</a></div>
  <div class="abs scroll-pill"><svg width="20" height="36" viewBox="0 0 20 36"><polyline points="6,14 10,18 14,14" fill="none" stroke="#0c1d31" stroke-width="1.6"/><polyline points="6,19 10,23 14,19" fill="none" stroke="#0c1d31" stroke-width="1.6"/></svg></div>
</header>

<!-- SOURCES -->
<section class="sources">
  <svg class="edge" viewBox="0 0 1200 70" preserveAspectRatio="none"><polygon points="0,0 1200,0 0,0" fill="#0c1d31"/><polygon points="600,0 1200,0 1200,0" fill="#0a1727"/></svg>
  <h2 class="abs center section-title" style="top:64px">Your patients’ full medical history<br>from all sources</h2>
  <p class="abs center section-lead" style="top:142px">Corvanta clinical data network has unprecedented reach across the continuum of care.</p>

  <svg class="icon" style="left:342px;top:202px" width="46" height="46" viewBox="0 0 46 46" fill="none" stroke="#5b7fd0" stroke-width="1.6"><rect x="4" y="4" width="16" height="12"/><rect x="26" y="4" width="16" height="12"/><rect x="15" y="28" width="16" height="12"/><path d="M12 16v6h22v-6M23 22v6"/></svg>
  <div class="source left" style="top:258px"><h3>EMR Networks</h3>Connected to 800,000 Physician EMR databases and over 60,000 hospitals across the country.</div>

  <svg class="icon" style="left:812px;top:196px" width="42" height="48" viewBox="0 0 42 48" fill="none" stroke="#5b7fd0" stroke-width="1.6"><rect x="10" y="4" width="26" height="34"/><rect x="5" y="10" width="26" height="34" fill="#0c2b4c"/><path d="M10 18h16M10 24h16M10 30h12"/></svg>
  <div class="source right" style="top:258px"><h3>RX Data or US Pharmacies</h3>Comprehensive medication history including medication starts, adherence, and switching behavior is collected from national and regional pharmacy data feeds. This includes specialized pharmacies.</div>

  <svg class="icon" style="left:344px;top:444px" width="44" height="40" viewBox="0 0 44 40" fill="none" stroke="#5b7fd0" stroke-width="1.6"><rect x="3" y="3" width="38" height="26"/><path d="M8 17h8l3-7 5 13 3-6h9M16 36h12M22 29v7"/></svg>
  <div class="source left" style="top:496px"><h3>Diagnostic Labs</h3>Corvanta is directly connected to all major diagnostic testing laboratories, enabling collection of all lab results.</div>

  <svg class="icon" style="left:806px;top:434px" width="56" height="56" viewBox="0 0 56 56" fill="none" stroke="#5b7fd0" stroke-width="1.6"><circle cx="28" cy="28" r="6"/><circle cx="10" cy="10" r="4"/><circle cx="46" cy="10" r="4"/><circle cx="10" cy="46" r="4"/><circle cx="46" cy="46" r="4"/><path d="M13 13l10 10M43 13L33 23M13 43l10-10M43 43L33 33"/></svg>
  <div class="source right" style="top:496px"><h3>HIE Networks</h3>Aggregating from 32 Health Information Exchange networks for real-time access to clinical data.</div>

  <svg class="icon" style="left:338px;top:640px" width="48" height="54" viewBox="0 0 48 54" fill="none" stroke="#5b7fd0" stroke-width="1.6"><rect x="12" y="4" width="24" height="16"/><rect x="4" y="20" width="40" height="20"/><rect x="12" y="34" width="24" height="16"/><path d="M16 40h16M16 45h12"/></svg>
  <div class="source left" style="top:706px"><h3>Provider Faxes</h3>Fax records received from PCPs and specialists are converted into structured, searchable electronic records (C-CD) for ingestion into the Corvanta Lumora™.</div>

  <svg class="icon" style="left:812px;top:642px" width="46" height="54" viewBox="0 0 46 54" fill="none" stroke="#5b7fd0" stroke-width="1.6"><rect x="4" y="4" width="30" height="10"/><rect x="4" y="18" width="30" height="10"/><rect x="4" y="32" width="30" height="10"/><circle cx="36" cy="44" r="6"/><path d="M40 48l4 4"/></svg>
  <div class="source right" style="top:706px"><h3>Claims Databases</h3>Connected to the nation’s largest clearinghouses for open and closed claims submission and processing, including Medicare Part A, B and D data for 53 million Medicare beneficiaries. This includes Medical &amp; Rx Open/Closed Claims EDI and Remittance ERI.</div>
</section>

<!-- TRANSFORM -->
<section class="transform">
  <svg class="edge" viewBox="0 0 1200 70" preserveAspectRatio="none"><polygon points="0,0 1200,0 1200,40" fill="#0b2744"/></svg>
  <h2 class="abs center section-title" style="top:156px">Transformed into 1 composite C-CDA heath record</h2>
  <p class="abs center section-lead" style="top:198px">The Corvanta synthesis engine utilizes OCR, advanced parsing techniques, Clinical Natural Language Processing (cNLP), proprietary logic<br>and NPI matching to clean, de-duplicate, structure and enrich all inputs from data acquisition.</p>
  <p class="abs center section-lead" style="top:246px">The normalized data is unified into the Lumora C-CDA, an enhanced composite longitudinal record in C-CDA format, the industry standard<br>for all interoperability initiatives</p>
  <svg class="abs front" style="left:554px;top:323px" width="92" height="92" viewBox="0 0 92 92"><circle cx="46" cy="46" r="42" fill="#0c1d31" stroke="#b7a5cd" stroke-width="3"/><rect x="30" y="30" width="32" height="32" fill="#22d1b4"/></svg>
  <div class="abs ccda-frame front">
    <div class="ccda-panel" role="img" aria-label="Lumora C-CDA record screen">
      <div class="ccda-head"></div>
      <h4>C-CDA</h4>
      <p>The normalized data is unified into the Lumora C-CDA, an enhanced composite longitudinal record in C-CDA format, the industry standard for all interoperability initiatives</p>
    </div>
  </div>
</section>

<!-- INSIGHTS -->
<section class="insights">
  <h2 class="abs center section-title" style="top:78px">Summarized and linked to key insights</h2>
  <p class="abs center section-lead" style="top:118px">Insights are presented in a concise summary with direct links to supporting evidence. HCC, HEDIS and MIPS opportunities are abstracted and cross-linked<br>directly to the original text in the underlying record for quick and easy reference.</p>

  <div class="feature-ring front" style="left:140px;top:230px"><svg width="40" height="40" viewBox="0 0 40 40" fill="none" stroke="#22d1b4" stroke-width="1.6"><circle cx="20" cy="20" r="15"/><path d="M20 20l7-7"/><circle cx="20" cy="20" r="2" fill="#22d1b4"/></svg></div>
  <div class="insight" style="top:324px"><h3>Risk-Adjustment</h3>HCC opportunities for new capture and recapture are identified and extracted using logic algorithms.</div>

  <div class="feature-ring front" style="left:140px;top:450px"><svg width="40" height="40" viewBox="0 0 40 40" fill="none" stroke="#22d1b4" stroke-width="1.8"><path d="M6 18a20 20 0 0 1 28 0M11 23a13 13 0 0 1 18 0"/><circle cx="20" cy="30" r="3"/></svg></div>
  <div class="insight" style="top:540px"><h3>Quality Analysis</h3>HEDIS and MIPS quality measure gaps closed using NQAB certified technology to generate QRDAIII.</div>

  <div class="shot front" style="left:452px;top:232px;width:296px;height:314px" role="img" aria-label="Lumora summary screen with HCC, HEDIS and MIPS findings and View Source buttons"></div>
  <div class="shot framed front" style="left:845px;top:182px;width:213px;height:124px" role="img" aria-label="Source document: progress note"></div>
  <div class="shot framed front" style="left:845px;top:347px;width:213px;height:166px" role="img" aria-label="Source document: lab report"></div>
  <div class="shot framed front" style="left:845px;top:546px;width:213px;height:124px" role="img" aria-label="Source document: medication table"></div>
</section>

<!-- EHR -->
<section class="ehr">
  <div class="vendor-grid">
    <div class="vendor"><span class="dot"></span>Alderscript</div>
    <div class="vendor">Helionhealth</div>
    <div class="vendor">Tessaro</div>
    <div class="vendor">Emberly</div>
    <div class="vendor">Medrilo</div>
    <div class="vendor">Fernpath</div>
    <div class="vendor" style="font-size:12px">Orwell Health</div>
    <div class="vendor">Vantira</div>
  </div>
  <h2 class="abs ehr-title">Delivered directly into<br>your EHR for native<br>viewing</h2>
  <p class="abs ehr-copy">The final package is delivered as a single longitudinal record into each patient’s chart within your EHR, viewable natively</p>
</section>

<!-- FEATURES -->
<section class="features">
  <div class="card" style="left:140px;height:235px">
    <svg width="70" height="70" viewBox="0 0 70 70" fill="none" stroke="#6f8fe0" stroke-width="2"><path d="M35 8v14M35 48v14M8 35h14M48 35h14M16 16l9 9M45 45l9 9M54 16l-9 9M25 45l-9 9"/><rect x="30" y="30" width="10" height="10" transform="rotate(45 35 35)" fill="#ffffff" stroke="none"/></svg>
    <h3>1-CLICK ACCESS</h3>
    <p>1-click access to each inference and insight in the underlying record</p>
  </div>
  <div class="card active" style="left:377px;height:255px">
    <svg width="70" height="70" viewBox="0 0 70 70" fill="none" stroke="#ffffff" stroke-width="2"><circle cx="35" cy="35" r="30"/><circle cx="35" cy="35" r="18"/><rect x="30" y="30" width="10" height="10" transform="rotate(45 35 35)" fill="#ffffff" stroke="none"/></svg>
    <h3>SEARCHABLE</h3>
    <p style="color:#fff">All data in the Lumora CCDA is searchable, including previously unstructured data</p>
  </div>
  <div class="card" style="left:613px;height:275px">
    <svg width="70" height="70" viewBox="0 0 70 70" fill="none" stroke="#6f8fe0" stroke-width="2"><path d="M16 20a26 26 0 1 0 12-10"/><polyline points="12,12 16,20 24,18"/><rect x="30" y="30" width="10" height="10" transform="rotate(45 35 35)" fill="#ffffff" stroke="none"/></svg>
    <h3>SEAMLESS<br>INTEGRATION</h3>
    <p>Designed for seamless integration into your current tools and workflow</p>
  </div>
  <div class="card" style="left:850px;height:300px">
    <svg width="76" height="70" viewBox="0 0 76 70" fill="none" stroke-width="2"><circle cx="30" cy="35" r="26" stroke="#6f8fe0"/><circle cx="46" cy="35" r="26" stroke="#886aae"/><rect x="33" y="30" width="10" height="10" transform="rotate(45 38 35)" fill="#ffffff"/></svg>
    <h3>EMPOWER<br>PHYSICIANS</h3>
    <p>Provide physicians with a complete summarized medical history linked to supporting documentation ahead of every encounter</p>
  </div>
</section>

<!-- BLOG -->
<section class="blog">
  <svg class="edge" viewBox="0 0 1200 70" preserveAspectRatio="none"><polygon points="0,0 1200,0 0,45" fill="#0c1d31"/></svg>
  <h2 class="abs center section-title" style="top:48px">Latest Bolg</h2>
  <article class="post" style="left:140px">
    <div class="photo" role="img" aria-label="Photo of caring hands holding an older patient's hands" style="background:linear-gradient(135deg,#c9b6a8,#8e7a6e)"></div>
    <div class="date">25<small>DEC</small></div>
    <h4>Lorem Ipsum is dummy text of the printing &amp; Lorem.</h4>
    <p>Lorem Ipsum is simply dummy text of the ok printing and typesetting.</p>
    <span class="more">READ MORE →</span>
  </article>
  <article class="post" style="left:458px">
    <div class="photo" role="img" aria-label="Photo of a doctor listening with a stethoscope" style="background:linear-gradient(135deg,#e8e4e0,#b9b2ab)"></div>
    <div class="date">24<small>DEC</small></div>
    <h4>Lorem Ipsum is dummy text of the printing &amp; Lorem.</h4>
    <p>Lorem Ipsum is simply dummy text of the ok printing and typesetting.</p>
    <span class="more">READ MORE →</span>
  </article>
  <article class="post" style="left:776px">
    <div class="photo" role="img" aria-label="Photo of a patient embracing a family member" style="background:linear-gradient(135deg,#c7dbe4,#d8a98c)"></div>
    <div class="date">23<small>DEC</small></div>
    <h4>Lorem Ipsum is dummy text of the printing &amp; Lorem.</h4>
    <p>Lorem Ipsum is simply dummy text of the ok printing and typesetting.</p>
    <span class="more">READ MORE →</span>
  </article>
  <div class="abs center" style="top:470px"><a class="btn">Request Access</a></div>
</section>
<div class="arrow" style="left:74px"><svg width="12" height="12" viewBox="0 0 12 12"><polyline points="8,2 4,6 8,10" fill="none" stroke="#22d1b4" stroke-width="2"/></svg></div>
<div class="arrow" style="left:1092px"><svg width="12" height="12" viewBox="0 0 12 12"><polyline points="4,2 8,6 4,10" fill="none" stroke="#22d1b4" stroke-width="2"/></svg></div>

<!-- ABOUT -->
<footer class="about">
  <svg class="edge" viewBox="0 0 1200 70" preserveAspectRatio="none"><polygon points="0,0 1200,0 1200,30" fill="#0d2f52"/></svg>
  <p class="abs center" style="top:55px">The Corvanta Lumora is a game-changing tool designed to accelerate success in value-based contracts by maximizing outcomes, scores and<br>revenue while significantly decreasing inefficiencies and administrative burden.</p>
  <p class="abs center" style="top:105px">Corvanta platform has been shaped by our partnerships with the leaders in value-based care to address their most complex challenges. We are experts<br>in interoperability technology who are passionate about empowering healthcare organizations to achieve market-leading results.</p>
</footer>
<div class="legal">© Copyright CORVANTA 2021 | All Rights Reserved.</div>

</div>
</body>
</html>
```